Website redesign

We need a bold revamp of our website (http://www.brantocksparkworks.co.nz/)
which at the moment looks dated. We want a crisp, fresh and bold look. The background image behind web page can go. Open to complete new layout

Target Market(s)

Electrical contracting company- working in the domestic and commercial field

Coding

Coded - Design and coding required

Number of Pages Required

5+ page

Font styles to use
Sans Serif

Colors

Designer to choose colors to be used in the design.

```html
<!DOCTYPE html>
<html lang="en">
<head>
<meta charset="utf-8">
<title>Brantock Sparkworks — Electrical services</title>
<link rel="stylesheet" href="https://fonts.googleapis.com/css2?family=Lato:wght@400;700&display=swap">
<style>
  :root {
    --blue: #3e4af5;
    --blue-soft: #8c94f9;
    --ink: #151515;
    --nav: #333333;
    --muted: #9a9fa6;
    --white: #ffffff;
  }
  * { margin: 0; padding: 0; box-sizing: border-box; }
  html, body { width: 1200px; height: 1060px; overflow: hidden; background: var(--white); }
  body { font-family: "Lato", sans-serif; color: var(--ink); position: relative; }

  .site-header { position: absolute; top: 0; left: 0; width: 1200px; height: 88px; }
  .brand { position: absolute; left: 119px; top: 30px; display: flex; align-items: center; gap: 8px;
    font-size: 17px; font-weight: 700; color: var(--ink); line-height: 1.1; }
  .brand-mark { width: 14px; height: 14px; background: #e0201b; }
  .main-nav { position: absolute; left: 284px; top: 37px; display: flex; gap: 25px; }
  .main-nav a { font-size: 13.5px; color: var(--nav); text-decoration: none; letter-spacing: 0.2px; }
  .header-phone { position: absolute; right: 120px; top: 33px; display: flex; align-items: center; gap: 10px;
    font-size: 18px; font-weight: 700; color: var(--nav); }

  .hero { position: absolute; top: 88px; left: 0; width: 1200px; height: 445px;
    background: linear-gradient(100deg, #2c3037 0%, #4a5058 40%, #6f747b 70%, #55595f 100%); }
  .hero-photo { position: absolute; inset: 0; }
  .hero-content { position: absolute; left: 119px; top: 123px; color: var(--white); }
  .hero-title { font-size: 55px; font-weight: 700; line-height: 1; letter-spacing: -0.5px; }
  .hero-lead { margin-top: 26px; font-size: 17px; color: #d4d6d9; }
  .btn-primary { position: absolute; left: 1px; top: 130px; width: 141px; height: 45px; background: var(--blue);
    color: var(--white); font-size: 14px; font-weight: 700; display: flex; align-items: center; justify-content: center;
    border-radius: 2px; text-decoration: none; }

  .services { position: absolute; top: 533px; left: 0; width: 1200px; height: 527px; }
  .section-rule { position: absolute; left: 582px; top: 47px; width: 38px; height: 3px; background: var(--blue); }
  .section-title { position: absolute; top: 58px; width: 100%; text-align: center; font-size: 34px; font-weight: 700; }
  .service { position: absolute; top: 163px; width: 228px; }
  .service-icon { display: block; width: 54px; height: 54px; }
  .service h3 { font-size: 19.5px; font-weight: 400; margin-top: 30px; color: var(--ink); }
  .service p { margin-top: 12px; font-size: 15px; line-height: 26.4px; color: var(--muted); }
  .btn-outline { position: absolute; left: 541px; top: 430px; width: 119px; height: 44px; border: 2px solid var(--blue);
    border-radius: 3px; color: var(--blue); font-size: 14.5px; display: flex; align-items: center; justify-content: center;
    text-decoration: none; }
</style>
</head>
<body>
  <header class="site-header">
    <div class="brand"><span class="brand-mark"></span>Brantock<br>Sparkworks</div>
    <nav class="main-nav">
      <a href="#">HOME</a><a href="#">ABOUT US</a><a href="#">SERVICES</a><a href="#">PROJECTS</a><a href="#">CONTACT US</a>
    </nav>
    <div class="header-phone">
      <svg width="14" height="16" viewBox="0 0 24 24" aria-hidden="true"><path fill="#333" d="M6.6 10.8a15 15 0 0 0 6.6 6.6l2.2-2.2c.3-.3.7-.4 1-.2 1.1.4 2.3.6 3.6.6.6 0 1 .4 1 1V20c0 .6-.4 1-1 1A17 17 0 0 1 3 4c0-.6.4-1 1-1h3.5c.6 0 1 .4 1 1 0 1.3.2 2.5.6 3.6.1.3 0 .7-.2 1z"/></svg>
      0800 55 41 72
    </div>
  </header>

  <section class="hero">
    <div class="hero-photo" role="img" aria-label="Electrician in a blue cap working on a switchboard, dimmed behind the heading"></div>
    <div class="hero-content">
      <h1 class="hero-title">Electrical services</h1>
      <p class="hero-lead">Lorem ipsum dolor sit amet, consectetur adipiscing elit, sed do eiusmod tempor.</p>
      <a class="btn-primary" href="#">Contact us</a>
    </div>
  </section>

  <section class="services">
    <div class="section-rule"></div>
    <h2 class="section-title">Our services</h2>

    <article class="service" style="left:121px">
      <svg class="service-icon" viewBox="0 0 54 54" aria-hidden="true">
        <path d="M16 24v-7a11 11 0 0 1 22 0v7" fill="none" stroke="var(--blue)" stroke-width="5"/>
        <rect x="10" y="24" width="34" height="26" rx="4" fill="var(--blue)"/>
        <rect x="25" y="32" width="4" height="10" rx="2" fill="#fff"/>
      </svg>
      <h3>Security</h3>
      <p>Lorem ipsum dolor sit amet, consectetur adipiscing elit, sed do eiusmod tempor incididunt ut labore et dolore magna aliqua</p>
    </article>

    <article class="service" style="left:366px">
      <svg class="service-icon" viewBox="0 0 54 54" aria-hidden="true">
        <rect x="21" y="4" width="12" height="34" rx="6" fill="none" stroke="var(--blue)" stroke-width="4"/>
        <circle cx="27" cy="42" r="9" fill="var(--blue)"/>
        <rect x="25" y="18" width="4" height="22" fill="var(--blue)"/>
      </svg>
      <h3>Heat pumps</h3>
      <p>Lorem ipsum dolor sit amet, consectetur adipiscing elit, sed do eiusmod tempor incididunt ut labore</p>
    </article>

    <article class="service" style="left:611px">
      <svg class="service-icon" viewBox="0 0 54 54" aria-hidden="true">
        <path d="M27 6c-9 0-14 7-14 15v11l-5 7h38l-5-7V21c0-8-5-15-14-15z" fill="var(--blue)"/>
        <circle cx="27" cy="45" r="5" fill="var(--blue)"/>
      </svg>
      <h3>Alarms</h3>
      <p>Lorem ipsum dolor sit amet, consectetur adipiscing elit, sed do eiusmod tempor</p>
    </article>

    <article class="service" style="left:857px">
      <svg class="service-icon" viewBox="0 0 54 54" aria-hidden="true">
        <rect x="4" y="8" width="46" height="32" rx="3" fill="var(--blue)"/>
        <rect x="9" y="13" width="36" height="22" fill="#fff"/>
        <rect x="17" y="44" width="20" height="4" rx="2" fill="var(--blue)"/>
      </svg>
      <h3>TV</h3>
      <p>Lorem ipsum dolor sit amet, consectetur adipiscing elit, sed do eiusmod tempor incididunt ut labore et dolore</p>
    </article>

    <a class="btn-outline" href="#">More</a>
  </section>
</body>
</html>
```